Web design concept for a IT recruitment agency.

Our website addresses two different target groups:
- Customers (companies) wanting to hire new IT talent
- It talent to find a new JOB

We a looking for a visual design concept that either addresses both target groups in one of the following options:
a. target both groups in 1 single splash page.
b. target both groups in 2 different pages one for both groups
c. or any creative third concept you can come up with

Requirements, we want one overall visual concept, that both target groups can relate to.

Trigger words what we want to express:
- passion / drive
- knowhow
- involvement
- professional/yet playful
- engagement

Background, company culture:
We are a recruitment agency with over 15 years of experience, we have no hard-sale culture.
But we emphasize on long term relationships, showing real interest in people and their needs.

Design requirements:
Use logo
Flat contemporary design

Target Market(s)

Industry/Entity Type

Hire

Number of Pages Required

2 page

Requirements
Must have
• We a looking for a visual design concept that either addresses both target groups

```html
<!DOCTYPE html>
<html lang="en">
<head>
<meta charset="utf-8">
<title>Hirevale — IT Recruitment</title>
<link rel="stylesheet" href="https://fonts.googleapis.com/css2?family=Lato:wght@400;700;900&display=swap">
<style>
:root{
  --blue:#10a6ea;
  --blue-dark:#0a8fcc;
  --ink:#1d1d1d;
  --dark:#222426;
  --darker:#1a1b1c;
  --grey-band:#e9e9e9;
  --row-alt:#ededed;
  --text:#444;
  --muted:#8a8a8a;
  --white:#fff;
}
*{box-sizing:border-box;margin:0;padding:0}
html,body{width:1200px;height:4186px;overflow:hidden}
body{font-family:'Lato',sans-serif;color:var(--text);background:var(--white);position:relative}
a{color:inherit;text-decoration:none}
.btn{display:inline-flex;align-items:center;justify-content:center;background:var(--blue);color:var(--white);font-weight:700;font-size:13px;text-transform:uppercase;letter-spacing:.5px}
.btn-dark{background:var(--ink)}
.section{position:absolute;left:0;width:1200px}

/* header */
.site-header{top:0;height:103px;background:var(--white)}
.brand{position:absolute;left:112px;top:30px;display:flex;align-items:center;gap:10px}
.brand-dot{width:40px;height:40px;border-radius:50%;background:var(--blue)}
.brand-name{font-size:36px;font-weight:400;color:var(--ink)}
.account{position:absolute;right:98px;top:39px;display:flex;align-items:center;gap:30px;font-size:12px;font-weight:700;color:var(--ink);text-transform:uppercase}
.account .item{display:flex;align-items:center;gap:7px}
.account .btn{width:145px;height:42px;font-size:13px}

/* nav */
.main-nav{top:103px;height:70px;background:var(--dark);display:flex;align-items:center}
.nav-links{position:absolute;left:100px;top:0;height:70px;display:flex}
.nav-links a{display:flex;align-items:center;padding:0 17px;color:var(--white);font-size:13px;font-weight:700;text-transform:uppercase}
.nav-links a.active{background:var(--blue)}
.search{position:absolute;left:818px;top:18px;display:flex;gap:12px}
.search .field{width:214px;height:34px;background:#1a1b1c;border:1px solid #3a3b3d;color:#888;font-size:12px;padding:9px 10px}
.search .go{width:58px;height:34px;background:var(--blue);display:flex;align-items:center;justify-content:center}

/* hero */
.hero{top:173px;height:552px;background:linear-gradient(180deg,#2b2d2f 0%,#1f2021 100%)}
.hero-map{position:absolute;inset:0;background:radial-gradient(ellipse at 50% 35%,rgba(255,255,255,.05),rgba(255,255,255,0) 60%)}
.eyebrow{position:absolute;top:98px;left:0;width:1200px;display:flex;justify-content:center;align-items:center;gap:20px;color:var(--white);font-size:16px;font-weight:700;letter-spacing:1px}
.eyebrow span.line{width:110px;height:1px;background:rgba(255,255,255,.6)}
.hero h1{position:absolute;top:140px;width:1200px;text-align:center;color:var(--white);font-size:56px;font-weight:900}
.hero .tagline{position:absolute;top:222px;width:1200px;text-align:center;color:var(--white);font-size:20px;font-weight:700;letter-spacing:.5px}
.audience{position:absolute;top:343px;width:501px;height:209px;padding:28px 40px;text-align:center;color:var(--white)}
.audience.seekers{left:100px;background:#161718}
.audience.employers{left:600px;background:var(--blue)}
.audience h2{font-size:24px;font-weight:700;margin-bottom:14px}
.audience p{font-size:12px;line-height:1.6;margin-bottom:22px}
.audience .btn{width:137px;height:42px;font-size:12px}
.audience.seekers .btn{background:var(--blue)}
.audience.employers .btn{background:var(--white);color:var(--blue)}

/* stats */
.stats{top:725px;height:145px;background:var(--grey-band);display:flex;justify-content:center;align-items:center;gap:0}
.stat{width:246px;text-align:center;border-right:2px solid #cfcfcf}
.stat:last-child{border-right:none}
.stat .num{font-size:46px;font-weight:700;color:var(--blue);line-height:1}
.stat .label{font-size:18px;color:#a8a8a8;text-transform:uppercase;margin-top:8px}

/* jobs */
.jobs{top:870px;height:748px}
.section-title{text-align:center;color:var(--ink);font-weight:900;font-size:48px;letter-spacing:1px}
.section-sub{text-align:center;color:var(--ink);font-size:18px;letter-spacing:1px;text-transform:uppercase}
.jobs .section-title{margin-top:70px}
.jobs .section-sub{margin-top:6px}
.job-table{position:absolute;left:100px;top:224px;width:1002px;border:1px solid #e0e0e0;height:418px}
.job-head,.job-row{display:grid;grid-template-columns:330px 170px 150px 140px 100px 110px;align-items:center}
.job-head{height:42px;background:var(--blue);color:var(--white);font-size:11px;text-transform:uppercase}
.job-head span:first-child{padding-left:22px}
.job-head span:nth-child(n+2),.job-row > :nth-child(n+2){text-align:center}
.job-row{height:89px;border-bottom:1px solid #e3e3e3;font-size:12px;font-weight:700;color:var(--ink);text-transform:uppercase}
.job-row:nth-child(3){background:var(--row-alt)}
.job-row .title{padding-left:22px}
.job-row .loc,.job-row .pay{font-weight:400;font-size:11px}
.tag{display:inline-block;padding:3px 8px;font-size:10px;color:var(--white);background:var(--ink)}
.tag.part{background:var(--blue)}
.job-row .btn{width:96px;height:34px;font-size:11px}
.see-all{position:absolute;left:507px;top:617px;width:188px;height:52px;font-size:15px;text-transform:none}

/* trigger */
.trigger{top:1618px;height:659px;background:linear-gradient(100deg,#1d1e1f 0%,#2e2f30 55%,#3b3a38 100%);overflow:hidden}
.trigger-scene{position:absolute;inset:0;background:radial-gradient(ellipse at 70% 35%,rgba(120,110,95,.35),rgba(0,0,0,0) 60%)}
.phone{position:absolute;left:106px;top:67px;width:368px;height:640px;border-radius:52px;background:#f4f4f4;border:3px solid #d8d8d8}
.phone-screen{position:absolute;left:18px;top:74px;width:360px;height:560px;background:var(--white);overflow:hidden}
.phone-head{height:2px;background:var(--blue)}
.phone-cols{display:grid;grid-template-columns:95px 135px 100px;height:48px;align-items:center;font-size:11px;color:var(--ink);text-transform:uppercase;border-bottom:1px solid #ddd;padding-left:32px}
.phone-row{display:grid;grid-template-columns:125px 135px 100px;height:88px;align-items:center;font-size:12px;font-weight:700;color:var(--ink);border-bottom:1px solid #e3e3e3;padding-left:18px;text-transform:uppercase}
.phone-row .loc{font-weight:400;font-size:11px}
.phone-row .tag{justify-self:center}
.phone-btn{position:absolute;left:72px;top:478px;width:188px;height:50px;font-size:15px;text-transform:none}
.trigger-copy{position:absolute;left:608px;top:60px;width:500px;color:var(--white)}
.trigger-copy h2{font-size:56px;font-weight:900;letter-spacing:1px}
.trigger-copy .sub{font-size:20px;margin-top:4px;letter-spacing:.5px}
.trigger-copy p{font-size:12px;line-height:1.9;margin-top:36px;width:460px}
.words{list-style:none;margin-top:40px;width:470px}
.words li{display:flex;align-items:center;gap:26px;height:51px;border-bottom:1px solid rgba(255,255,255,.25);font-size:17px;font-weight:700;text-transform:uppercase}
.words li:last-child{border-bottom:none}
.words .n{width:28px;height:28px;border-radius:50%;background:var(--blue);font-size:13px;display:flex;align-items:center;justify-content:center}

/* posts */
.posts{top:2277px;height:759px}
.posts .section-title{margin-top:88px;font-size:44px}
.posts .section-sub{margin-top:8px;font-size:13px}
.post{position:absolute;top:240px;width:321px}
.post .photo{height:203px;background:linear-gradient(135deg,#c9c2b6,#8d8474 60%,#5f5a52)}
.post h3{margin-top:26px;font-size:17px;font-weight:700;line-height:1.4;color:var(--ink)}
.post .meta{margin-top:10px;font-size:12px;color:var(--muted)}
.post .meta span{margin-left:18px}
.post p{margin-top:12px;font-size:12px;line-height:1.6;color:#777}
.post .btn{margin-top:26px;width:105px;height:37px;font-size:12px;text-transform:none}

/* candidates */
.candidates{top:3036px;height:284px;background:var(--blue);color:var(--white);text-align:center}
.candidates h2{margin-top:50px;font-size:32px;font-weight:900}
.candidates p{margin:14px auto 0;width:620px;font-size:14px;line-height:1.5}
.people{position:absolute;top:3245px;left:0;width:1200px;height:187px}
.person{position:absolute;width:123px;height:187px;background:var(--white);border:1px solid #e3e3e3;text-align:center}
.person .portrait{height:125px;margin:4px;background:linear-gradient(180deg,#e3e6ea,#a9b0b8)}
.person .name{margin-top:15px;font-size:11px;font-weight:700;color:var(--blue)}
.person .role{margin-top:4px;font-size:10px;color:var(--muted)}
.partners{top:3488px;height:50px;display:flex;justify-content:center;gap:13px}
.badge{width:100px;height:50px;background:#f1f1f1;border:1px solid #e2e2e2}
.choice{top:3580px;height:131px;border-top:1px solid #e3e3e3;display:flex;justify-content:center;align-items:center;gap:20px;font-size:13px;font-weight:700;color:var(--ink);padding-bottom:18px}
.choice .btn{height:34px;font-size:12px;text-transform:none}
.choice .hire{width:156px}
.choice .find{width:120px}

/* footer */
.site-footer{top:3711px;height:475px;background:var(--darker);color:var(--white)}
.fcol{position:absolute;top:42px}
.fcol h4{font-size:18px;font-weight:700;margin-bottom:20px}
.fcol ul{list-style:none}
.fcol li{font-size:12px;line-height:25px;color:#ccc}
.fcol p{font-size:12px;line-height:1.7;color:#bbb;width:330px}
.fcol .btn{margin-top:22px;width:126px;height:36px;font-size:12px}
.footer-rule{position:absolute;top:279px;left:0;width:1200px;height:1px;background:#333}
.social{position:absolute;top:329px;left:0;width:1200px;display:flex;justify-content:center;gap:20px}
.social span{width:50px;height:50px;border-radius:50%;border:2px solid var(--white)}
.copyright{position:absolute;top:412px;width:1200px;text-align:center;font-size:15px;color:#ddd}
</style>
</head>
<body>

<header class="section site-header">
  <div class="brand"><span class="brand-dot"></span><span class="brand-name">Hirevale</span></div>
  <div class="account">
    <span class="item">
      <svg width="12" height="14" viewBox="0 0 12 14"><rect x="1" y="6" width="10" height="8" rx="1" fill="#1d1d1d"/><path d="M3 6V4a3 3 0 0 1 6 0v2" stroke="#1d1d1d" stroke-width="1.8" fill="none"/></svg>
      Sign up</span>
    <span class="item">
      <svg width="13" height="14" viewBox="0 0 13 14"><circle cx="6.5" cy="4" r="3.5" fill="#1d1d1d"/><path d="M0 14a6.5 6 0 0 1 13 0z" fill="#1d1d1d"/></svg>
      Login</span>
    <a class="btn" href="#">Create Resume</a>
  </div>
</header>

<nav class="section main-nav">
  <div class="nav-links">
    <a class="active" href="#">Home</a><a href="#">How it work</a><a href="#">Jobs seekers</a><a href="#">Employers</a><a href="#">Blog</a><a href="#">Contact us</a>
  </div>
  <div class="search">
    <div class="field">Search...</div>
    <div class="go"><svg width="16" height="16" viewBox="0 0 16 16"><circle cx="6.5" cy="6.5" r="5" stroke="#fff" stroke-width="2" fill="none"/><path d="M10.5 10.5 15 15" stroke="#fff" stroke-width="2"/></svg></div>
  </div>
</nav>

<section class="section hero">
  <div class="hero-map" role="img" aria-label="Faint world map texture"></div>
  <div class="eyebrow"><span class="line"></span>HIREVALE<span class="line"></span></div>
  <h1>LOOKING FOR A JOB?</h1>
  <div class="tagline">THERE'S NO BETTER PLACE TO START</div>
  <div class="audience seekers">
    <h2>Easiest way to find your dream job</h2>
    <p>It is a long established fact that a reader will be distracted by the readable content of a page when looking at its layout.</p>
    <a class="btn" href="#">Find a Job</a>
  </div>
  <div class="audience employers">
    <h2>Hire Skilled People, best of them</h2>
    <p>It is a long established fact that a reader will be distracted by the readable content of a page when looking at its layout.</p>
    <a class="btn" href="#">Post a Job</a>
  </div>
</section>

<section class="section stats">
  <div class="stat"><div class="num">4329</div><div class="label">Members</div></div>
  <div class="stat"><div class="num">894</div><div class="label">Jobs</div></div>
  <div class="stat"><div class="num">1482</div><div class="label">Resumes</div></div>
  <div class="stat"><div class="num">83</div><div class="label">Companies</div></div>
</section>

<section class="section jobs">
  <h2 class="section-title">FIND A JOBS</h2>
  <div class="section-sub">Your job for a future</div>
  <div class="job-table">
    <div class="job-head"><span>Job title</span><span>By</span><span>Option</span><span>Location</span><span>Sallery</span><span></span></div>
    <div class="job-row"><span class="title">PHP Developer</span><span>Norbrook</span><span><span class="tag">Full time</span></span><span class="loc">New York City</span><span class="pay">35$</span><span><a class="btn btn-dark" href="#">Apply now</a></span></div>
    <div class="job-row"><span class="title">Web Developer</span><span>Quillon</span><span><span class="tag part">Part time</span></span><span class="loc">New York City</span><span class="pay">35$</span><span><a class="btn" href="#">Apply now</a></span></div>
    <div class="job-row"><span class="title">Hardware Engineer</span><span>Veltra</span><span><span class="tag">Full time</span></span><span class="loc">New York City</span><span class="pay">35$</span><span><a class="btn btn-dark" href="#">Apply now</a></span></div>
    <div class="job-row"><span class="title">Frontend Developer</span><span>Brightlane</span><span><span class="tag">Weekend</span></span><span class="loc">New York City</span><span class="pay">35$</span><span><a class="btn btn-dark" href="#">Apply now</a></span></div>
  </div>
  <a class="btn see-all" href="#">See All Jobs</a>
</section>

<section class="section trigger">
  <div class="trigger-scene" role="img" aria-label="Dim photo of a person working at a laptop in an office"></div>
  <div class="phone">
    <div class="phone-screen">
      <div class="phone-head"></div>
      <div class="phone-cols"><span>By</span><span>Option</span><span>Loca</span></div>
      <div class="phone-row"><span>Norbrook</span><span class="tag">Full time</span><span class="loc">NEW YO</span></div>
      <div class="phone-row"><span>Quillon</span><span class="tag part">Part time</span><span class="loc">NEW YO</span></div>
      <div class="phone-row"><span>Veltra</span><span class="tag">Full time</span><span class="loc">NEW YO</span></div>
      <div class="phone-row"><span>Brightlane</span><span class="tag">Weekend</span><span class="loc">NEW YO</span></div>
      <a class="btn phone-btn" href="#">See All Jobs</a>
    </div>
  </div>
  <div class="trigger-copy">
    <h2>TRIGGER WORDS</h2>
    <div class="sub">WHAT WE WANT TO EXPRESS</div>
    <p>Lorem Ipsum is simply dummy text of the printing and typesetting industry. Lorem Ipsum has been the industry's standard dummy text ever since the 1500s, when an unknown printer took a galley of type and scrambled it to make a type specimen book.</p>
    <ul class="words">
      <li><span class="n">1</span>Passion / Drive</li>
      <li><span class="n">2</span>Know-how</li>
      <li><span class="n">3</span>Nvolvement</li>
      <li><span class="n">4</span>Professional/yet playful</li>
      <li><span class="n">5</span>Engagement</li>
    </ul>
  </div>
</section>

<section class="section posts">
  <h2 class="section-title">LATEST POSTS</h2>
  <div class="section-sub">Specially crafted job posts everyday</div>
  <article class="post" style="left:100px">
    <div class="photo" role="img" aria-label="Photo of a business team standing together"></div>
    <h3>Hey Job Seeker, It's Time To Get Up And Get Hired</h3>
    <div class="meta">October 10, 2015<span>0 Comments</span></div>
    <p>The world of job seeking can be all consuming. From secretly stalking the open reqs page of your dream company to sending endless applications.</p>
    <a class="btn" href="#">Read More</a>
  </article>
  <article class="post" style="left:438px">
    <div class="photo" role="img" aria-label="Photo of colleagues meeting around a laptop"></div>
    <h3>Hey Job Seeker, It's Time To Get Up And Get Hired</h3>
    <div class="meta">October 10, 2015<span>0 Comments</span></div>
    <p>The world of job seeking can be all consuming. From secretly stalking the open reqs page of your dream company to sending endless applications.</p>
    <a class="btn" href="#">Read More</a>
  </article>
  <article class="post" style="left:778px">
    <div class="photo" role="img" aria-label="Photo of a smiling professional at a desk"></div>
    <h3>Hey Job Seeker, It's Time To Get Up And Get Hired</h3>
    <div class="meta">October 10, 2015<span>0 Comments</span></div>
    <p>The world of job seeking can be all consuming. From secretly stalking the open reqs page of your dream company to sending endless applications.</p>
    <a class="btn" href="#">Read More</a>
  </article>
</section>

<section class="section candidates">
  <h2>FIND YOUR BEST CANDIDATE</h2>
  <p>Donec tincidunt felis quam, eu tempus purus finibus in. Curabitur hendrerit, odio in viverra interdum, lorem velit scelerisque ipsum, a sagittis ligula leo in dolor. Etiam vestibulum.</p>
</section>
<div class="people">
  <div class="person" style="left:170px"><div class="portrait" role="img" aria-label="Candidate portrait"></div><div class="name">Tomas Hale</div><div class="role">Java Developer</div></div>
  <div class="person" style="left:318px"><div class="portrait" role="img" aria-label="Candidate portrait"></div><div class="name">Tomas Hale</div><div class="role">Web Developer</div></div>
  <div class="person" style="left:465px"><div class="portrait" role="img" aria-label="Candidate portrait"></div><div class="name">Tomas Hale</div><div class="role">Frontend Developer</div></div>
  <div class="person" style="left:613px"><div class="portrait" role="img" aria-label="Candidate portrait"></div><div class="name">Tomas Hale</div><div class="role">Backend Developer</div></div>
  <div class="person" style="left:760px"><div class="portrait" role="img" aria-label="Candidate portrait"></div><div class="name">Tomas Hale</div><div class="role">IT Manager</div></div>
  <div class="person" style="left:908px"><div class="portrait" role="img" aria-label="Candidate portrait"></div><div class="name">Tomas Hale</div><div class="role">Java Developer</div></div>
</div>

<div class="section partners">
  <span class="badge"></span><span class="badge"></span><span class="badge"></span><span class="badge"></span>
  <span class="badge"></span><span class="badge"></span><span class="badge"></span><span class="badge"></span>
</div>

<div class="section choice">
  <span>I want to</span>
  <a class="btn hire" href="#">Hire Employee</a>
  <span>or</span>
  <a class="btn find" href="#">Find Job</a>
</div>

<footer class="section site-footer">
  <div class="fcol" style="left:100px">
    <h4>About</h4>
    <p>Donec tincidunt felis quam, eu tempus purus finibus in. Curabitur hendrerit, odio in viverra interdum, lorem velit scelerisque ipsum, a sagittis ligula leo in dolor. Etiam vestibulum.</p>
    <a class="btn" href="#">Get Started</a>
  </div>
  <div class="fcol" style="left:552px">
    <h4>Company</h4>
    <ul><li>Home</li><li>How it work</li><li>Jobs seekers</li><li>Employers</li><li>Blog</li><li>Contact us</li></ul>
  </div>
  <div class="fcol" style="left:748px">
    <h4>Press</h4>
    <ul><li>In the News</li><li>Press Releases</li><li>Awards</li><li>Testimonials</li><li>Timeline</li></ul>
  </div>
  <div class="fcol" style="left:943px">
    <h4>Browse</h4>
    <ul><li>Freelancers by Category</li><li>Freelancers in USA</li><li>Freelancers in UK</li><li>Freelancers in Canada</li><li>Freelancers in Australia</li><li>Find Jobs</li></ul>
  </div>
  <div class="footer-rule"></div>
  <div class="social"><span></span><span></span><span></span><span></span><span></span></div>
  <div class="copyright">Copyright © 2015. All Rights Reserved.</div>
</footer>

</body>
</html>
```